Feldwind Atelier GmbH needs a Letterhead

Need a Letter/Card head based on the logo and Webpage design.
To be used for Business letters and One-Page Handouts with the discription of our different Services.
Cards to be used as Flyers to print on different Topics.
Should be Topic nutral as we do Sabbatical-Consultancy, Coaching, Job-Coaching and Vision-Board Workshops (more to come). See www.feldwindatelier.ch

Target Market(s)

Individuales who need Sabbatical-Support/Coaching/JOB-Coaching
Companies who want to give me a mandate as Business Coach

Industry/Entity Type

Business

Font styles to use
Other font styles liked:
• Verdana

Colors
9ccb3b
3277b5
aaaaaa
eaeaea

Requirements
Must have
• Background White or light gray
• not to big/present the Information on Company-Adresse/phone/email/web/offices
• Use the Logo (chair) in a creative way
• Please use following Colors:
• Green: R141, G198, B63
• Blue: R28, G117, B188
• Darkgray: R109, G110, B113
• Lightgray: R209, G211, B212
Should not have
• Wrong Colors!
• Use mentioned Color codes above.

```html
<!DOCTYPE html>
<html lang="de">
<head>
<meta charset="utf-8">
<title>Feldwind Atelier – Briefpapier</title>
<link href="https://fonts.googleapis.com/css2?family=Carlito:wght@400;700&family=Montserrat:wght@400;500&display=swap" rel="stylesheet">
<style>
  :root {
    --green: #8dc63f;
    --blue: #1c75bc;
    --dark-gray: #6d6e71;
    --light-gray: #d1d3d4;
    --stage: #a3a3a3;
    --paper: #ffffff;
    --ink: #2b2b2b;
  }
  * { margin: 0; padding: 0; box-sizing: border-box; }
  html, body { width: 1200px; height: 1200px; overflow: hidden; }
  body { background: var(--stage); position: relative; }

  .letterhead {
    position: absolute;
    left: 211px; top: 45px;
    width: 778px; height: 1110px;
    background: var(--paper);
    box-shadow: 0 6px 24px rgba(0,0,0,0.25);
    overflow: hidden;
  }

  .brand {
    position: absolute; left: 78px; top: 100px;
    display: flex; align-items: center; gap: 12px;
  }
  .brand-mark { width: 26px; height: 26px; background: var(--green); }
  .brand-name {
    font-family: "Carlito", sans-serif; font-weight: 700;
    font-size: 30px; color: var(--dark-gray); letter-spacing: 0.5px;
  }

  .sender {
    position: absolute; top: 70px; left: 420px;
    display: flex; gap: 24px;
    font-family: "Montserrat", sans-serif; font-size: 10px; line-height: 1.35;
    color: var(--ink);
  }
  .sender-block { border-left: 1px solid var(--blue); padding-left: 8px; }
  .sender-label { color: var(--blue); }

  .letter-body {
    position: absolute; left: 130px; top: 290px; width: 560px;
    font-family: "Carlito", sans-serif; font-size: 15px; line-height: 26px;
    color: var(--ink);
  }
  .salutation { margin-bottom: 22px; }
  .letter-body p { margin-bottom: 22px; }
  .closing { margin-top: 12px; }
  .signature {
    display: block; width: 180px; height: 70px; margin: 8px 0 4px;
    background: linear-gradient(90deg, #e9e9e9, #f4f4f4);
  }

  .contact-bar {
    position: absolute; left: 0; right: 0; bottom: 0; height: 34px;
    background: var(--blue);
    display: flex; justify-content: flex-end; align-items: center; gap: 18px;
    padding-right: 48px;
    font-family: "Montserrat", sans-serif; font-size: 10px; color: #fff;
  }
</style>
</head>
<body>
  <main class="letterhead">
    <header>
      <div class="brand">
        <span class="brand-mark"></span>
        <span class="brand-name">Feldwind Atelier</span>
      </div>
      <div class="sender">
        <div class="sender-block">
          <div class="sender-label">Firmenanschrift:</div>
          <div>Feldwind Atelier GmbH</div>
          <div>Lena Bachmann</div>
          <div>Wiesenstrasse 14, 8466 Trüllikon</div>
          <div>Schweiz</div>
        </div>
        <div class="sender-block">
          <div class="sender-label">Büros:</div>
          <div>Trüllikon</div>
          <div>Weinland</div>
          <div>am Dorfplatz</div>
          <div>Winterthur</div>
        </div>
      </div>
    </header>

    <section class="letter-body">
      <div class="salutation">Lorem Ipsum is simply</div>
      <p>dummy text of the printing and typesetting industry. Lorem Ipsum has been the industry's standard dummy text ever since the 1500s, when an unknown printer took a galley of type and scrambled it to make a type specimen book. It has survived not only five centuries, but also the leap into electronic typesetting, remaining essentially unchanged. It was popularised in the 1960s with the release of Stellwerk sheets containing Lorem Ipsum passages, and more recently with desktop publishing software like Satzmeister Pro including versions of Lorem Ipsum.</p>
      <p>It is a long established fact that a reader will be distracted by the readable content of a page when looking at its layout. The point of using Lorem Ipsum is that it has a more-or-less normal distribution of letters, as opposed to using 'Content here, content here', making it look like readable English. Many desktop publishing packages and web page editors now use.</p>
      <p>Contrary to popular belief, Lorem Ipsum is not simply random text. It has roots in a piece of classical Latin literature from 45 BC, making it over 2000 years old. Jonas Riedweg, a Latin professor at Talbrunnen College in Lindmark, looked up one of the more obscure Latin words, consectetur, from a Lorem Ipsum passage, and going through the cites of the word in classical literature, discovered the undoubtable source. Lorem Ipsum comes from sections 1.10.32 and 1.10.33 of "de Limitibus Rerum et Verborum" (The Limits of Things and Words) by Marcellus Orin, written in 45 BC. This book</p>
      <div class="closing">Lorem Ipsum</div>
      <span class="signature" role="img" aria-label="Handschriftliche Unterschrift"></span>
      <div>Lorem Ipsum is a dummy</div>
    </section>

    <footer class="contact-bar">
      <span>P: +41 (0) 79 000 12 34</span>
      <span>E: lena.bachmann@feldwindatelier.ch</span>
      <span>W: www.feldwindatelier.ch</span>
    </footer>
  </main>
</body>
</html>
```